Rising Paths Web Design

I am starting a new company that will provide LIFE COACHING services - I have tried to design a website, but it's too complicated. Right now, it's just me - I'm the only person that will provide services through the website - I have used artmarket to purchase a logo (see below). I want to be able to update the website myself, but need a template - basic design. Because I am not technologically savvy enough to explain in words - I basically want to have a website that will provide basic information about my services (coaching), a page about me and my background, hopefully scheduling possibilities, and testimonials — also a page for writing/blogs. I bought a website through NetHarbor - so when I have a template, I guess I”d use that - but maybe I’ll need to work with a designer to actually get it up on the internet. I have a head shot that I’ll upload, too.
Target Market(s)
Clients from the independent (private school) world - teachers, administrators
Number of Pages Required
4 page
Look and feel
Each slider illustrates characteristics of the customer's brand and the style your logo design should communicate.

```html
<!DOCTYPE html>
<html lang="en">
<head>
<meta charset="utf-8">
<title>Rising Paths Coaching</title>
<link rel="stylesheet" href="https://fonts.googleapis.com/css2?family=Cormorant+Garamond:wght@500;600&family=Jost:wght@400;500;600&display=swap">
<style>
:root{
  --teal:#00ad8e;
  --teal-dark:#00987d;
  --mint:#dff3ef;
  --mint-soft:#e8f5f2;
  --grey-bg:#f7f7f7;
  --ink:#111111;
  --body:#555555;
  --line:#e6e6e6;
  --white:#ffffff;
  --serif:"Cormorant Garamond",Georgia,serif;
  --sans:"Jost",Arial,sans-serif;
}
*{box-sizing:border-box;margin:0;padding:0}
html,body{width:1200px;height:5009px;overflow:hidden}
body{font-family:var(--sans);color:var(--ink);background:var(--white)}
section,header,footer{position:relative;width:1200px}
.abs{position:absolute}
.serif{font-family:var(--serif);font-weight:500}
.btn-dark{background:var(--ink);color:var(--white);font-weight:600;font-size:13px;letter-spacing:.5px;display:flex;align-items:center;justify-content:center}
.btn-outline{border:2px solid var(--ink);color:var(--ink);font-weight:600;font-size:13px;letter-spacing:.5px;display:flex;align-items:center;justify-content:center;background:var(--white)}
.link-teal{color:var(--teal);font-size:11px;font-weight:500;letter-spacing:.4px;border-bottom:1px solid var(--teal);padding-bottom:2px}
.center-title{left:0;width:1200px;text-align:center;font-size:50px}
.photo{border-radius:0}

/* header */
.site-header{height:107px;background:var(--white)}
.brand-box{left:86px;top:0;width:167px;height:132px;background:var(--white);box-shadow:0 2px 10px rgba(0,0,0,.08);display:flex;flex-direction:column;align-items:center;justify-content:center;gap:8px;z-index:2}
.brand-dot{width:34px;height:34px;border-radius:50%;border:2px solid var(--teal)}
.brand-name{font-family:var(--serif);font-weight:600;font-size:18px;color:#2f6f66}
.main-nav{left:440px;top:44px;display:flex;gap:38px;font-size:13px;color:#444}
.main-nav .active{color:var(--teal)}
.header-icons{left:990px;top:44px;display:flex;gap:14px;align-items:center}
.header-icons span{width:12px;height:12px;border-radius:50%;background:var(--teal)}

/* hero */
.hero{height:539px;background:var(--mint);overflow:hidden}
.hero-title{left:86px;top:112px;font-size:62px;line-height:78px;width:700px}
.hero-text{left:86px;top:287px;width:620px;font-size:14px;line-height:23px;color:var(--body)}
.hero-btn{left:86px;top:356px;width:184px;height:55px}
.signature-area{left:300px;top:362px;width:196px;height:46px;background:rgba(0,0,0,.06);border-radius:4px}
.hero-photo{left:768px;top:19px;width:342px;height:520px;background:linear-gradient(180deg,#cfe9e3,#f4f4f4 60%,#e7e7e7)}

/* about */
.about{height:517px;background:var(--grey-bg)}
.about-mark{left:560px;top:102px;width:80px;height:80px;border-radius:50%;border:1px solid #bfded7;display:flex;align-items:center;justify-content:center;font-family:var(--serif);font-size:11px;font-weight:600;color:#2f6f66}
.about-title{top:190px}
.about-text{left:230px;top:266px;width:740px;text-align:center;font-size:14px;line-height:23px;color:var(--body)}
.about-btn{left:505px;top:360px;width:190px;height:60px}

/* services */
.services{height:757px;background:var(--white)}
.services-title{top:95px}
.service-card{top:181px;width:325px;text-align:center}
.service-img{width:325px;height:260px;position:relative}
.tag{position:absolute;top:26px;right:22px;background:var(--teal);color:var(--white);font-size:11px;padding:4px 14px;border-radius:14px}
.service-name{font-family:var(--serif);font-weight:600;font-size:21px;line-height:25px;margin-top:23px}
.service-text{font-size:12.5px;line-height:21px;color:var(--body);margin:14px auto 0;width:300px}
.service-btn{width:150px;height:58px;margin:32px auto 0}

/* schedule */
.schedule{height:898px;background:var(--grey-bg)}
.schedule-title{top:90px}
.feature{left:86px;top:190px;width:1027px;height:270px;background:var(--white);box-shadow:0 2px 14px rgba(0,0,0,.05)}
.feature-img{left:0;top:0;width:513px;height:270px;background:linear-gradient(90deg,#6fa15b,#c9d6a6 50%,#7fa868)}
.feature-date{left:553px;top:40px;display:flex;align-items:center;gap:10px;color:var(--teal);font-size:17px}
.feature-text{left:553px;top:82px;width:430px;font-size:26px;line-height:35px}
.feature-btn{left:553px;top:178px;width:152px;height:46px;font-size:13px}
.event-row{left:86px;width:1027px;height:112px;background:var(--white);box-shadow:0 2px 14px rgba(0,0,0,.05)}
.event-day{left:0;top:0;width:138px;height:112px;border-right:2px solid var(--line);display:flex;flex-direction:column;align-items:center;justify-content:center;color:var(--teal);font-weight:600}
.event-day b{font-size:37px;line-height:38px}
.event-day small{font-size:15px}
.event-time{left:176px;top:30px;color:var(--teal);font-size:12px}
.event-text{left:176px;top:52px;font-size:24px}
.event-link{right:46px;top:42px}
.view-all{left:571px;top:782px}

/* testimonial */
.testimonial{height:707px;background:var(--white)}
.testi-band{left:86px;top:100px;width:1027px;height:457px;background:var(--teal)}
.testi-photo{left:583px;top:92px;width:332px;height:465px;background:linear-gradient(180deg,#8a5a3c,#c79a7b 45%,#f1ede8)}
.testi-card{left:163px;top:194px;width:362px;height:415px;background:var(--white);box-shadow:0 4px 18px rgba(0,0,0,.08)}
.quote-mark{left:26px;top:22px}
.testi-quote{left:50px;top:52px;width:260px;font-size:19px;line-height:28px;font-weight:500}
.testi-name{left:50px;top:332px;font-size:14px;font-weight:500}
.testi-role{left:68px;top:354px;font-size:10px;color:var(--body)}
.testi-arrows{left:974px;top:506px;display:flex;gap:18px}

/* news */
.news{height:690px;background:var(--grey-bg)}
.news-title{top:95px}
.news-card{top:188px;width:325px;height:403px;background:var(--white);box-shadow:0 2px 14px rgba(0,0,0,.05)}
.news-img{left:19px;top:19px;width:287px;height:192px}
.news-date{left:199px;top:162px;width:70px;height:60px;background:var(--teal);color:var(--white);font-weight:600;display:flex;flex-direction:column;align-items:center;justify-content:center;line-height:20px}
.news-date b{font-size:20px}
.news-date small{font-size:15px}
.news-author{left:29px;top:239px;display:flex;align-items:center;gap:8px;color:var(--teal);font-size:15px}
.news-text{left:29px;top:276px;width:270px;font-family:var(--serif);font-weight:500;font-size:20px;line-height:25px}
.news-link{left:29px;top:348px}

/* newsletter */
.newsletter{height:375px;background:var(--mint-soft);overflow:hidden}
.bubble{position:absolute;border-radius:50%;background:rgba(0,80,60,.06)}
.news-head{top:92px}
.news-sub{left:0;top:168px;width:1200px;text-align:center;font-size:13px;color:var(--body)}
.subscribe{left:348px;top:214px;width:502px;height:62px;background:var(--white);display:flex;align-items:center;justify-content:space-between;padding:0 26px;font-size:13px}
.subscribe .ph{color:#777}
.subscribe .go{color:var(--teal);font-weight:600;font-size:11px;display:flex;align-items:center;gap:8px}

/* footer */
.site-footer{height:419px;background:var(--white)}
.foot-brand{left:86px;top:96px;display:flex;align-items:center;gap:10px}
.foot-brand .brand-dot{width:30px;height:30px}
.foot-brand .brand-name{font-size:17px}
.foot-contact{left:86px;font-size:12.5px;font-weight:500;color:#333}
.foot-links{font-size:12px;font-weight:500;letter-spacing:.4px;color:#444}
.foot-social{left:966px;top:95px;display:flex;gap:13px}
.foot-social span{width:40px;height:40px;border-radius:50%;border:1px solid #bbb}
.foot-bottom{font-size:12px;color:#666;top:350px}
</style>
</head>
<body>

<header class="site-header">
  <div class="abs brand-box">
    <span class="brand-dot"></span>
    <span class="brand-name">Rising Paths</span>
  </div>
  <nav class="abs main-nav">
    <span class="active">Home</span><span>About Me</span><span>My Services</span><span>Schedule</span><span>Testimonials</span><span>Blog</span>
  </nav>
  <div class="abs header-icons">
    <span></span><span></span><span></span>
    <svg width="16" height="16" viewBox="0 0 16 16" fill="none" stroke="#333" stroke-width="1.5"><circle cx="7" cy="7" r="5"/><path d="M11 11l4 4"/></svg>
  </div>
</header>

<section class="hero">
  <h1 class="abs serif hero-title">“Always Push Yourself to the Next Level”</h1>
  <p class="abs hero-text">If you are not willing to risk the usual, you will have to settle for the ordinary. I'm here to help and share my story.</p>
  <div class="abs btn-dark hero-btn">GET FREE SESSION</div>
  <div class="abs signature-area" role="img" aria-label="Handwritten signature"></div>
  <div class="abs hero-photo" role="img" aria-label="Portrait of the coach with arms crossed"></div>
</section>

<section class="about">
  <div class="abs about-mark">Rising Paths</div>
  <h2 class="abs serif center-title about-title">Hello, I’m Maren Holt</h2>
  <p class="abs about-text">Lorem ipsum dolor sit amet, consectetur adipiscing elit. Suspendisse sed interdum leo. Sed pretium eleifend risus nec sagittis. Quisque laoreet purus aliquam, mattis metus vitae, ornare tellus. Curabitur bibendum facilisis mauris, sed varius enim pretium ut. Mauris bibendum ex erat, nec volutpat est vulputate non.</p>
  <div class="abs btn-outline about-btn">READ MY STORY</div>
</section>

<section class="services">
  <h2 class="abs serif center-title services-title">My Most Beloved Services</h2>
  <article class="abs service-card" style="left:86px">
    <div class="service-img" role="img" aria-label="Woman in a personal coaching session" style="background:linear-gradient(135deg,#c9b8a6,#e9e4df)"><span class="tag">One to One</span></div>
    <h3 class="service-name">Personal Sessions and Workshops</h3>
    <p class="service-text">Lorem ipsum dolor sit amet, consectetur adipiscing elit. Suspendisse sed interdum leo.</p>
    <div class="btn-outline service-btn">ENROLL NOW</div>
  </article>
  <article class="abs service-card" style="left:438px">
    <div class="service-img" role="img" aria-label="Clipboard with notes on a pink desk" style="background:linear-gradient(135deg,#f2c9bd,#f7e3dc)"><span class="tag">Public</span></div>
    <h3 class="service-name">Public Program for Individuals<br>and Teams</h3>
    <p class="service-text">Lorem ipsum dolor sit amet, consectetur adipiscing elit. Suspendisse sed interdum leo.</p>
    <div class="btn-outline service-btn">ENROLL NOW</div>
  </article>
  <article class="abs service-card" style="left:788px">
    <div class="service-img" role="img" aria-label="Tablet and notebook on a desk" style="background:linear-gradient(135deg,#d9d9d6,#f0efec)"><span class="tag">Online</span></div>
    <h3 class="service-name">Learn Secrets to Peak Performance</h3>
    <p class="service-text">Lorem ipsum dolor sit amet, consectetur adipiscing elit. Suspendisse sed interdum leo.</p>
    <div class="btn-outline service-btn">ENROLL NOW</div>
  </article>
</section>

<section class="schedule">
  <h2 class="abs serif center-title schedule-title">Upcoming Schedule</h2>
  <div class="abs feature">
    <div class="abs feature-img" role="img" aria-label="Group of smiling women outdoors"></div>
    <div class="abs feature-date">
      <svg width="22" height="22" viewBox="0 0 22 22" fill="none" stroke="#00ad8e" stroke-width="1.5"><rect x="2" y="4" width="18" height="16" rx="2"/><path d="M2 9h18M7 2v4M15 2v4"/></svg>
      July 30, 2022 | 12:00 P.M.
    </div>
    <p class="abs serif feature-text">Ut lobortis in nunc vel auctor. Etiam id maximus mauris.</p>
    <div class="abs btn-outline feature-btn">VIEW DETAILS</div>
  </div>
  <div class="abs event-row" style="top:488px">
    <div class="abs event-day"><b>31</b><small>JULY</small></div>
    <span class="abs event-time">12:00 PM</span>
    <p class="abs serif event-text">Ut lobortis in nunc vel auctor. Etiam id maximus mauris.</p>
    <span class="abs link-teal event-link">VIEW DETAILS</span>
  </div>
  <div class="abs event-row" style="top:628px">
    <div class="abs event-day"><b>31</b><small>JULY</small></div>
    <span class="abs event-time">12:00 PM</span>
    <p class="abs serif event-text">Ut lobortis in nunc vel auctor. Etiam id maximus mauris.</p>
    <span class="abs link-teal event-link">VIEW DETAILS</span>
  </div>
  <span class="abs link-teal view-all">VIEW ALL</span>
</section>

<section class="testimonial">
  <div class="abs testi-band"></div>
  <div class="abs testi-photo" role="img" aria-label="Smiling client portrait"></div>
  <div class="abs testi-card">
    <svg class="abs quote-mark" width="110" height="80" viewBox="0 0 110 80"><path d="M8 10c0-6 5-10 12-10h20v10H24c-4 0-6 3-6 8v62H0V20zM60 10c0-6 5-10 12-10h20v10H76c-4 0-6 3-6 8v62H52V20z" fill="#d9efe9"/></svg>
    <p class="abs testi-quote">Donec pellentesque laoreet quam. Praesent maximus ligula ornare imperdiet placerat. Donec ut finibus elit. Nulla consectetur convallis suscipit.</p>
    <span class="abs testi-name">— Nora Bell</span>
    <span class="abs testi-role">CEO at Brightwell</span>
  </div>
  <div class="abs testi-arrows">
    <svg width="34" height="14" viewBox="0 0 34 14" fill="none" stroke="#cfcfcf" stroke-width="2"><path d="M33 7H2M8 1L2 7l6 6"/></svg>
    <svg width="34" height="14" viewBox="0 0 34 14" fill="none" stroke="#111" stroke-width="2"><path d="M1 7h31M26 1l6 6-6 6"/></svg>
  </div>
</section>

<section class="news">
  <h2 class="abs serif center-title news-title">Latest News &amp; Updates</h2>
  <article class="abs news-card" style="left:86px">
    <div class="abs news-img" role="img" aria-label="Notebook and coffee on a desk" style="background:linear-gradient(135deg,#5a4636,#d8d2c8)"></div>
    <div class="abs news-date"><b>31</b><small>JULY</small></div>
    <div class="abs news-author"><svg width="16" height="16" viewBox="0 0 16 16" fill="#00ad8e"><circle cx="8" cy="5" r="4"/><path d="M0 16c0-5 4-7 8-7s8 2 8 7z"/></svg>By Admin</div>
    <p class="abs news-text">Lorem ipsum dolor sit amet, consectetur adipiscing</p>
    <span class="abs link-teal news-link">READ MORE</span>
  </article>
  <article class="abs news-card" style="left:438px">
    <div class="abs news-img" role="img" aria-label="Coach talking with a client" style="background:linear-gradient(135deg,#b7c8d6,#e8e4de)"></div>
    <div class="abs news-date"><b>31</b><small>JULY</small></div>
    <div class="abs news-author"><svg width="16" height="16" viewBox="0 0 16 16" fill="#00ad8e"><circle cx="8" cy="5" r="4"/><path d="M0 16c0-5 4-7 8-7s8 2 8 7z"/></svg>By Admin</div>
    <p class="abs news-text">Lorem ipsum dolor sit amet, consectetur adipiscing</p>
    <span class="abs link-teal news-link">READ MORE</span>
  </article>
  <article class="abs news-card" style="left:788px">
    <div class="abs news-img" role="img" aria-label="Person walking up steps" style="background:linear-gradient(180deg,#e9b9a6,#f3ddd2)"></div>
    <div class="abs news-date"><b>31</b><small>JULY</small></div>
    <div class="abs news-author"><svg width="16" height="16" viewBox="0 0 16 16" fill="#00ad8e"><circle cx="8" cy="5" r="4"/><path d="M0 16c0-5 4-7 8-7s8 2 8 7z"/></svg>By Admin</div>
    <p class="abs news-text">Lorem ipsum dolor sit amet, consectetur adipiscing</p>
    <span class="abs link-teal news-link">READ MORE</span>
  </article>
</section>

<section class="newsletter">
  <span class="bubble" style="left:-40px;top:70px;width:170px;height:170px"></span>
  <span class="bubble" style="left:160px;top:30px;width:90px;height:90px"></span>
  <span class="bubble" style="left:150px;top:140px;width:70px;height:70px"></span>
  <span class="bubble" style="left:20px;top:240px;width:100px;height:100px"></span>
  <span class="bubble" style="left:250px;top:260px;width:40px;height:40px"></span>
  <span class="bubble" style="left:960px;top:60px;width:120px;height:120px"></span>
  <span class="bubble" style="left:940px;top:225px;width:105px;height:105px"></span>
  <span class="bubble" style="left:1100px;top:270px;width:160px;height:160px"></span>
  <h2 class="abs serif center-title news-head">Subscribe Newsletter</h2>
  <p class="abs news-sub">Get exclusive content sent directly by me</p>
  <div class="abs subscribe">
    <span class="ph">Enter Email</span>
    <span class="go">SUBSCRIBE <svg width="16" height="10" viewBox="0 0 16 10" fill="none" stroke="#00ad8e" stroke-width="1.5"><path d="M0 5h14M10 1l4 4-4 4"/></svg></span>
  </div>
</section>

<footer class="site-footer">
  <div class="abs foot-brand"><span class="brand-dot"></span><span class="brand-name">Rising Paths</span></div>
  <span class="abs foot-contact" style="top:208px">hello@risingpaths-mail.com</span>
  <span class="abs foot-contact" style="top:246px">(555) 010 2048</span>
  <span class="abs foot-contact" style="top:284px">Enter your address here</span>
  <span class="abs foot-links" style="left:531px;top:97px">MY STORY</span>
  <span class="abs foot-links" style="left:531px;top:144px">MY SCHEDULE</span>
  <span class="abs foot-links" style="left:531px;top:192px">SERVICES</span>
  <span class="abs foot-links" style="left:700px;top:97px">TESTIMONIALS</span>
  <span class="abs foot-links" style="left:700px;top:144px">NEWS</span>
  <span class="abs foot-links" style="left:700px;top:192px">CONTACT</span>
  <span class="abs foot-links" style="left:865px;top:97px">FAQs</span>
  <span class="abs foot-links" style="left:865px;top:144px">T &amp; C</span>
  <div class="abs foot-social" aria-label="Social links"><span></span><span></span><span></span></div>
  <span class="abs foot-bottom" style="left:86px">Copyright 2022.All right reserved.</span>
  <span class="abs foot-bottom" style="left:956px">Privacy Policy</span>
  <span class="abs foot-bottom" style="left:1066px">Sitemap</span>
</footer>

</body>
</html>
```